Ad for GP newsletter service

We are looking for a 'cut through' ad to advertise our national patient newsletter to GP (doctors) who run small practices around Australia.

The publication is published quarterly and is designed for patients to read while they are in the waiting room and has health articles as well as a comic and a reader giveaway.

A link to our latest edition can be found here http://flipreadhub.example/cliniccourier2012/docs/clinic_courier_winter_web_2013

The publication has been around for 16 years and is well respected however, like other print publications, numbers are dropping and GPs are looking to cut costs.
The other big selling point for this quarterly newsletter was that it helped meet the subscriber practice's accreditation requirements - now many don't bother with accreditation so that level is weaker.

We want to show GPs that providing trusted , peer reviewed health information is worth their investment - and that our service now offers to send the newsletter electronically to their patients (convenience and better reach) and that we can integrate with a practice website and other tools such as online videos.

The audience is quite conservative, though, and we are trying to drag them into a new way of looking at technology etc.

The key messages are - Clinic Courier subscription is worth the investment (because it is a value add to patients, they enjoy reading it) and that Clinic Courier can offer a range of support services such as integrating the newsletter with an affordable website and even advising on social media options.

The dimensions of ¼ pg ad are 15cmsx3col (15cms)

One possible idea would be using the 'Clinic Courier' newsletter as a 'cure' for an impatient waiting room ie. have a before and after shot showing a grumpy patient waiting then a happy patient reading the newsletter

Or

Showing a reader as smarter/ better informed than a non reader
Updates

Hi Guys, 

After thinking through this , I think there are potentially 3 different ads we want to run. 
The 3 concepts/ cells I want to create and test are:
a) Clinic Courier ..is at your fingertips. Displaying the product in tablet (ie. online / web), email and printed form
b) A shot of a doctor's surgery/ practice with the text 'Impatient' with the first two letters crossed out in red and the product / newsletter displayed 
c) Can your practice newsletter do this ? And show the newsletter juggling the following items in symbolic form : 
 - Accreditation
- Email copy to patients
- practice website 

Target Market(s)

Single practice GPs (doctors) and medical centers up to 10 doctors

Industry/Entity Type

Investment

Requirements
Must have
• Clinic Courier logo
Contact details
Must grab the reader's attention
Must be thought provoking and challenge assumptions

```html
<!DOCTYPE html>
<html lang="en">
<head>
<meta charset="utf-8">
<title>Clinic Courier – Ad</title>
<link rel="stylesheet" href="https://fonts.googleapis.com/css2?family=Fira+Sans+Extra+Condensed:wght@600;700&family=Open+Sans:ital,wght@0,400;0,800;1,700&display=swap">
<style>
  :root{
    --sky:#2196d3;
    --navy:#062a6e;
    --yellow:#ffd800;
    --white:#ffffff;
    --ink:#0a2a6b;
    --link-blue:#1f8fd0;
    --photo-a:#f3efe9;
    --photo-b:#c9b6a4;
  }
  *{margin:0;padding:0;box-sizing:border-box}
  html,body{width:1200px;height:1200px;overflow:hidden;background:var(--white)}
  .ad{position:relative;width:1200px;height:1200px;font-family:"Open Sans",Arial,sans-serif}
  .masthead{position:absolute;left:0;top:0;width:762px;height:403px;background:var(--sky)}
  .brand-name{position:absolute;left:28px;top:18px;color:var(--yellow);font-weight:800;font-size:132px;line-height:150px;text-transform:uppercase;letter-spacing:-3px}
  .tagline{position:absolute;left:40px;top:356px;color:var(--white);font-style:italic;font-weight:700;font-size:33px;line-height:44px}
  .family-photo{position:absolute;left:762px;top:0;width:438px;height:403px;background:linear-gradient(160deg,var(--photo-a) 0%,var(--photo-b) 100%)}
  .benefits{position:absolute;left:0;top:403px;width:1200px;height:632px;background:var(--navy);padding-top:70px}
  .benefit{position:relative;padding-left:100px;margin-bottom:20px}
  .benefit-title{font-family:"Fira Sans Extra Condensed","Arial Narrow",sans-serif;font-weight:600;font-size:51px;line-height:58px;color:var(--yellow)}
  .benefit-title::before{content:"";position:absolute;left:51px;top:20px;width:22px;height:22px;border:4px solid var(--yellow);border-radius:50%}
  .benefit-text{color:var(--white);font-size:29.5px;line-height:40px}
  .service-list{list-style:none;color:var(--white);font-size:29.5px;line-height:41px}
  .service-list li::before{content:"-";display:inline-block;width:31px}
  .contact{position:absolute;left:0;top:1035px;width:1200px;height:165px;background:var(--white)}
  .phone{position:absolute;left:46px;top:1056px;font-family:"Fira Sans Extra Condensed","Arial Narrow",sans-serif;font-weight:700;font-size:110px;line-height:120px;color:var(--ink);white-space:nowrap;transform:scaleX(0.7);transform-origin:left center}
  .divider{position:absolute;left:750px;top:1058px;width:3px;height:116px;background:var(--ink)}
  .address{position:absolute;left:788px;top:1060px;font-family:"Fira Sans Extra Condensed","Arial Narrow",sans-serif;font-weight:600;font-size:46px;line-height:58px;color:var(--link-blue);font-style:normal;white-space:nowrap}
</style>
</head>
<body>
<div class="ad">
  <header class="masthead">
    <div class="brand-name">Clinic<br>Courier</div>
    <p class="tagline">healthy advice from your family doctor</p>
  </header>
  <div class="family-photo" role="img" aria-label="Photo of a smiling family of four, children riding on their parents' shoulders, outdoors"></div>

  <section class="benefits">
    <div class="benefit">
      <h2 class="benefit-title">Clinic Courier subscription is worth the investment</h2>
      <p class="benefit-text">Providing trusted , peer reviewed health information is worth investment.</p>
    </div>
    <div class="benefit">
      <h2 class="benefit-title">Personalised stand-alone practice website</h2>
      <p class="benefit-text">Clinic Courier can provide a personalised stand-alone practice website<br>displaying your practice details, photos, logos, maps, links and more.</p>
    </div>
    <div class="benefit">
      <h2 class="benefit-title">Clinic Courier also offers a free e- health service</h2>
      <ul class="service-list">
        <li>Online Bookings</li>
        <li>SMS or email appointment reminders</li>
        <li>Prescription request (optional)</li>
        <li>Referral request (optional)</li>
      </ul>
    </div>
  </section>

  <footer class="contact"></footer>
  <div class="phone">Toll Free : 1800 555 019</div>
  <div class="divider"></div>
  <address class="address">PO BOX 412<br>Westmere NSW 2199</address>
</div>
</body>
</html>
```